rl ironcraft business card metallic look

revamp the existing design but want card to have a metalic look to it

Target Market(s)

construction industry

Industry/Entity Type

constrction

Contact Information for Business Card

front of card RL Ironcraft, phone 4163920857, email rl.ironcraftt@quellmail.example and instagram account; rl_ironcraft_

Font styles to use
Other font styles liked:
• masculine

Colors

Designer to choose only greyscale colors for use in the design.

Requirements
Must have
• back side RL Ironcraft then a list of everything : Siding, ACM Panels, Standing Seam,Soffit, Fascia, Gutters,Metal,Alu,inum, Viynyl, Metal Roofs and roof repairs
Nice to have
• I would like to keep the look of the existing card with the metal grids on the front
Should not have
• Need a design in two days

```html
<!DOCTYPE html>
<html lang="en">
<head>
<meta charset="utf-8">
<title>RL Ironcraft – Business Card</title>
<link href="https://fonts.googleapis.com/css2?family=Poppins:wght@300;400;600&display=swap" rel="stylesheet">
<style>
  :root {
    --backdrop: #3b3b3b;
    --card-light: #2e2e2e;
    --card-dark: #1f1f1d;
    --rule: #9a9a9a;
    --steel: #a6a6a6;
    --ink: #e6e6e6;
  }
  * { margin: 0; padding: 0; box-sizing: border-box; }
  html, body {
    width: 1021px; height: 1200px; overflow: hidden;
    background: var(--backdrop);
    font-family: "Poppins", sans-serif;
  }
  .card {
    position: absolute; left: 171px; width: 679px; height: 440px;
    background: linear-gradient(135deg, var(--card-light), var(--card-dark));
  }
  .card--front { top: 141px; }
  .card--back { top: 619px; }

  .rule { position: absolute; background: var(--rule); }
  .rule--top { left: 9px; top: 9px; width: 487px; height: 1px; }
  .rule--left { left: 9px; top: 9px; width: 1px; height: 125px; }
  .rule--bottom { left: 183px; top: 431px; width: 488px; height: 1px; }
  .rule--right { left: 670px; top: 305px; width: 1px; height: 127px; }

  .wordmark {
    position: absolute; color: var(--steel);
    font-weight: 600; letter-spacing: 1px; white-space: nowrap; line-height: 1;
  }
  .card--front .wordmark { left: 45px; top: 110px; font-size: 86px; }
  .card--back .wordmark { left: 246px; top: 110px; font-size: 58px; }

  .contact {
    position: absolute; left: 400px; top: 361px; list-style: none;
    color: var(--ink); font-weight: 300; font-size: 13.5px; white-space: nowrap;
  }
  .contact li { display: flex; align-items: center; height: 21px; }
  .contact svg { width: 16px; height: 16px; margin-right: 7px; flex: none; }
  .contact .handle-mark {
    width: 13px; height: 13px; margin: 0 9px 0 2px;
    border: 1.5px solid var(--ink); border-radius: 3px; flex: none;
  }

  .services {
    position: absolute; left: 48px; top: 46px; list-style: none;
    color: var(--ink); font-size: 19.5px; font-weight: 400;
  }
  .services li { display: flex; align-items: center; height: 35.3px; }
  .services svg { width: 15px; height: 15px; margin-right: 5px; flex: none; }
</style>
</head>
<body>

<section class="card card--front">
  <span class="rule rule--top"></span><span class="rule rule--left"></span>
  <span class="rule rule--bottom"></span><span class="rule rule--right"></span>

  <div class="wordmark">RL Ironcraft</div>

  <ul class="contact">
    <li>
      <svg viewBox="0 0 24 24" fill="var(--ink)" aria-hidden="true"><path d="M6.6 10.8a15.1 15.1 0 0 0 6.6 6.6l2.2-2.2a1 1 0 0 1 1-.25 11.4 11.4 0 0 0 3.6.57 1 1 0 0 1 1 1V20a1 1 0 0 1-1 1A17 17 0 0 1 3 4a1 1 0 0 1 1-1h3.5a1 1 0 0 1 1 1c0 1.250.2 2.450.57 3.57a1 1 0 0 1-.25 1z"/></svg>
      416-392-0857
    </li>
    <li>
      <svg viewBox="0 0 24 24" fill="none" stroke="var(--ink)" stroke-width="1.8" aria-hidden="true"><rect x="2.5" y="5" width="19" height="14" rx="1.5"/><path d="M3 6l9 7 9-7"/></svg>
      rl.ironcraftt@quellmail.example
    </li>
    <li><span class="handle-mark"></span>@rl_ironcraft_</li>
  </ul>
</section>

<section class="card card--back">
  <span class="rule rule--top"></span><span class="rule rule--left"></span>
  <span class="rule rule--bottom"></span><span class="rule rule--right"></span>

  <ul class="services">
    <li><svg viewBox="0 0 16 16" fill="none" stroke="var(--ink)" stroke-width="1.4"><path d="M2 14L14 2M9 2h5v5"/></svg>Siding</li>
    <li><svg viewBox="0 0 16 16" fill="none" stroke="var(--ink)" stroke-width="1.4"><path d="M2 14L14 2M9 2h5v5"/></svg>ACM Panels</li>
    <li><svg viewBox="0 0 16 16" fill="none" stroke="var(--ink)" stroke-width="1.4"><path d="M2 14L14 2M9 2h5v5"/></svg>Standing Seam</li>
    <li><svg viewBox="0 0 16 16" fill="none" stroke="var(--ink)" stroke-width="1.4"><path d="M2 14L14 2M9 2h5v5"/></svg>Soffit</li>
    <li><svg viewBox="0 0 16 16" fill="none" stroke="var(--ink)" stroke-width="1.4"><path d="M2 14L14 2M9 2h5v5"/></svg>Fascia</li>
    <li><svg viewBox="0 0 16 16" fill="none" stroke="var(--ink)" stroke-width="1.4"><path d="M2 14L14 2M9 2h5v5"/></svg>Gutters</li>
    <li><svg viewBox="0 0 16 16" fill="none" stroke="var(--ink)" stroke-width="1.4"><path d="M2 14L14 2M9 2h5v5"/></svg>Metal</li>
    <li><svg viewBox="0 0 16 16" fill="none" stroke="var(--ink)" stroke-width="1.4"><path d="M2 14L14 2M9 2h5v5"/></svg>Aluminum</li>
    <li><svg viewBox="0 0 16 16" fill="none" stroke="var(--ink)" stroke-width="1.4"><path d="M2 14L14 2M9 2h5v5"/></svg>Vinyl</li>
    <li><svg viewBox="0 0 16 16" fill="none" stroke="var(--ink)" stroke-width="1.4"><path d="M2 14L14 2M9 2h5v5"/></svg>Metal Roofs and Roof Repairs</li>
  </ul>

  <div class="wordmark">RL Ironcraft</div>
</section>

</body>
</html>
```